" Empresa nova no mercado, clínica ainda em fase de acabamento, pretendo oferecer consultas e exames a preços acessíveis, em ambiente confortável, seguro e acolhedor, com o compromisso de oferecer o melhor atendimento a cada paciente. "

```html
<!DOCTYPE html>
<html lang="pt-BR">
<head>
<meta charset="utf-8">
<title>Clinivita — Envelope e Papel Timbrado</title>
<link rel="stylesheet" href="https://fonts.googleapis.com/css2?family=Ubuntu:wght@400;500;700&display=swap">
<style>
  :root {
    --bg: #e9eaeb;
    --teal: #3a9ea0;
    --teal-dark: #2f8587;
    --teal-soft: rgba(255,255,255,0.08);
    --ink: #5f6468;
    --paper: #ffffff;
    --paper-mark: rgba(58,158,160,0.07);
  }
  * { margin: 0; padding: 0; box-sizing: border-box; }
  html, body { width: 1200px; height: 1200px; overflow: hidden; }
  body {
    background: var(--bg);
    font-family: "Ubuntu", Arial, sans-serif;
    position: relative;
  }
  .sheet {
    position: absolute;
    top: 270px;
    width: 440px;
    height: 640px;
    overflow: hidden;
    box-shadow: 0 14px 30px rgba(0,0,0,0.12);
  }
  /* Envelope back */
  .envelope { left: 130px; background: var(--teal); }
  .envelope__flap { position: absolute; inset: 0 0 auto 0; width: 100%; height: 70px; }
  .envelope__mark {
    position: absolute; width: 360px; height: 360px; border-radius: 50%;
    background: var(--teal-soft); right: -90px; top: 150px;
  }
  .envelope__contacts {
    position: absolute; left: 36px; bottom: 120px; list-style: none;
    color: #fff; font-size: 11px; line-height: 1;
  }
  .envelope__contacts li { display: flex; align-items: center; gap: 8px; margin-bottom: 11px; }
  .envelope__contacts svg { width: 11px; height: 11px; flex: none; }
  .envelope__brand {
    position: absolute; right: 36px; bottom: 112px;
    display: flex; align-items: center; gap: 8px;
    color: #fff; font-size: 26px; font-weight: 500;
  }
  .brand-dot { width: 20px; height: 20px; border-radius: 50%; background: currentColor; }
  .envelope__tagline {
    position: absolute; right: 36px; bottom: 96px; color: #fff;
    font-size: 7px; letter-spacing: 1.2px; opacity: .85;
  }
  /* Letterhead */
  .letterhead { left: 630px; background: var(--paper); }
  .letterhead__mark {
    position: absolute; width: 380px; height: 380px; border-radius: 50%;
    background: var(--paper-mark); left: -120px; top: 80px;
  }
  .letterhead__brand {
    position: absolute; left: 0; right: 0; top: 250px; text-align: center;
  }
  .letterhead__symbol {
    width: 40px; height: 40px; border-radius: 50%; background: var(--teal);
    margin: 0 auto 10px;
  }
  .letterhead__name { color: var(--teal); font-size: 46px; font-weight: 500; letter-spacing: -0.5px; }
  .letterhead__tagline {
    margin-top: 8px; color: var(--ink); font-size: 10.5px; letter-spacing: 2.2px;
  }
  .letterhead__band { position: absolute; left: 0; right: 0; bottom: 0; height: 10px; background: var(--teal); }
</style>
</head>
<body>
  <section class="sheet envelope" aria-label="Envelope">
    <svg class="envelope__flap" viewBox="0 0 440 70" preserveAspectRatio="none">
      <path d="M0 0 H440 V40 L410 70 H30 L0 40 Z" fill="var(--teal-dark)" opacity=".35"/>
      <path d="M0 40 L30 70 H410 L440 40" fill="none" stroke="#fff" stroke-opacity=".25"/>
    </svg>
    <div class="envelope__mark"></div>
    <ul class="envelope__contacts">
      <li><svg viewBox="0 0 12 12"><circle cx="6" cy="6" r="6" fill="#fff"/><rect x="3" y="4" width="6" height="4" fill="var(--teal)"/></svg>contato@clinivita.com.br</li>
      <li><svg viewBox="0 0 12 12"><circle cx="6" cy="6" r="6" fill="#fff"/><path d="M4 3 L5.5 4.8 L4.8 5.6 Q5.6 7 6.6 7.4 L7.4 6.6 L9 8 L8 9 Q5 9 3 5 Z" fill="var(--teal)"/></svg>(11) 3000-0000</li>
      <li><svg viewBox="0 0 12 12"><circle cx="6" cy="6" r="6" fill="#fff"/><path d="M4 3 L5.5 4.8 L4.8 5.6 Q5.6 7 6.6 7.4 L7.4 6.6 L9 8 L8 9 Q5 9 3 5 Z" fill="var(--teal)"/></svg>(11) 3000-0001</li>
      <li><svg viewBox="0 0 12 12"><circle cx="6" cy="6" r="6" fill="#fff"/><path d="M6 2.5 A2.3 2.3 0 0 1 8.3 4.8 C8.3 6.5 6 9.5 6 9.5 C6 9.5 3.7 6.5 3.7 4.8 A2.3 2.3 0 0 1 6 2.5 Z" fill="var(--teal)"/></svg>Rua das Flores, 100</li>
    </ul>
    <div class="envelope__brand"><span class="brand-dot"></span>Clinivita</div>
    <div class="envelope__tagline">SAÚDE ACESSÍVEL E ACOLHEDORA</div>
  </section>

  <section class="sheet letterhead" aria-label="Papel timbrado">
    <div class="letterhead__mark"></div>
    <div class="letterhead__brand">
      <div class="letterhead__symbol"></div>
      <div class="letterhead__name">Clinivita</div>
      <div class="letterhead__tagline">SAÚDE ACESSÍVEL E ACOLHEDORA</div>
    </div>
    <div class="letterhead__band"></div>
  </section>
</body>
</html>
```